PulseGuide business card

Create a warm & friendly yet professional business card.

2-sided.

I'm a PulseGuide, using VitaBeat to help people decrease stress, increase resiliency, and live a more heart-centered life. I want highlight VitaBeat in the card design.
The back of the card needs to show how your heart rate can change from a jagged pattern to a smooth pattern. You can use the 'frustration' and 'appreciation' graphics.
On the front, I really like the idea of a line going from the heart first as a jagged line then transforming to a smooth one (see graphic - I like the idea but not the colors/details of the heart + line graphic provided here). Can you create something nicer?

I used red font, but please feel free to change to other colors.

Target Market(s)

40-60 year old professional women, middle & upper middle class

Industry/Entity Type

Business

Requirements
Must have
• FRONT
VitaBeat logo ( from attached file - must also use the blue 'VitaBeat letters)
Registered trademark symbol after 'VitaBeat' the 1st time only
Merriwyn T. Hollingbeck, MSc, CWC, CSMCOSCA
Certified VitaBeat Practitioner & Licensed Provider, QRX7318
A primarily light background (white or another light color).

07835 964 027
Merriwyn@PulseGuide.co.uk
www.PulseGuide.co.uk

BACK - 'Frustration' and 'Appreciation' graphics (or the one graphic that shows them both)
Nice to have
• Graphic of a heart;
Graphic of a jagged-type line transforming to a smooth-type line;
Warm colors without being gaudy or too bold.

2 background colors with soft, elegant shading between the colors

Should not have
• Not more than 1 or 2 lines of light writing on a dark background.
Fonts smaller than 8.

Black or very dark background - it is ok for a small part of the card but please NOT for the majority of it.

```html
<!DOCTYPE html>
<html lang="en">
<head>
<meta charset="utf-8">
<title>PulseGuide business card</title>
<link rel="stylesheet" href="https://fonts.googleapis.com/css2?family=Arimo:wght@700&family=Open+Sans:wght@400&display=swap">
<style>
  :root {
    --page: #ffffff;
    --card: #e9ebf3;
    --magenta: #b0125f;
    --label: #a3145c;
    --blue-text: #3f62a3;
    --band-dark: #4a6aa8;
    --band-light: #7f97c5;
    --glow-core: rgba(61, 98, 176, 0.55);
    --glow-mid: rgba(61, 98, 176, 0.22);
    --glow-edge: rgba(61, 98, 176, 0);
    --trace: #ffffff;
  }
  * { margin: 0; padding: 0; box-sizing: border-box; }
  html, body { width: 954px; height: 1200px; overflow: hidden; background: var(--page); }
  body { position: relative; font-family: "Open Sans", Arial, sans-serif; }

  .side-label {
    position: absolute;
    font-family: "Open Sans", Arial, sans-serif;
    font-size: 27px;
    color: var(--label);
    line-height: 1;
  }
  .side-label--front { left: 57px; top: 56px; }
  .side-label--back { left: 830px; top: 1131px; }

  .card { position: absolute; background: var(--card); overflow: hidden; }
  .card--front { left: 60px; top: 112px; width: 827px; height: 447px; }
  .card--back { left: 63px; top: 656px; width: 826px; height: 449px; }
  .card__lines { position: absolute; inset: 0; width: 100%; height: 100%; display: block; }

  .pulse-area {
    position: absolute;
    background: radial-gradient(ellipse at center, var(--glow-core) 0%, var(--glow-mid) 45%, var(--glow-edge) 72%);
  }
  .pulse-area--front { left: 561px; top: 25px; width: 266px; height: 130px; }
  .pulse-area--upper { left: 272px; top: 15px; width: 360px; height: 93px; }
  .pulse-area--middle { left: 104px; top: 95px; width: 143px; height: 192px; }
  .pulse-area--lower { left: 558px; top: 238px; width: 268px; height: 136px; }

  .brand { position: absolute; display: flex; align-items: center; gap: 10px; }
  .brand__square { display: block; background: var(--magenta); }
  .brand__name {
    font-family: "Arimo", Arial, sans-serif;
    font-weight: 700;
    color: var(--magenta);
    line-height: 1;
  }
  .brand__reg { font-size: 0.5em; vertical-align: 0.9em; margin-left: 1px; }
  .brand--front { left: 27px; top: 63px; height: 40px; }
  .brand--front .brand__square { width: 34px; height: 34px; }
  .brand--front .brand__name { font-size: 31px; }
  .brand--back { left: 52px; top: 338px; height: 36px; }
  .brand--back .brand__square { width: 28px; height: 28px; }
  .brand--back .brand__name { font-size: 25px; }

  .role-title {
    position: absolute; left: 27px; top: 177px;
    font-family: "Arimo", Arial, sans-serif; font-weight: 700;
    font-size: 35px; color: var(--blue-text); line-height: 1.1;
  }
  .person-name {
    position: absolute; left: 27px; top: 221px;
    font-family: "Arimo", Arial, sans-serif; font-weight: 700;
    font-size: 27px; color: var(--blue-text); line-height: 1.1;
  }
  .credentials {
    position: absolute; left: 27px; top: 264px;
    font-size: 16px; color: var(--blue-text); line-height: 1.2;
  }
  .certification {
    position: absolute; left: 27px; top: 306px;
    font-size: 21px; color: var(--blue-text); line-height: 28px;
  }
  .certification__badge {
    display: inline-block; width: 46px; height: 24px;
    background: var(--magenta); border-radius: 4px;
    vertical-align: -3px; margin-right: 8px;
  }
  .certification__line2 { display: block; padding-left: 6px; }

  .contact {
    position: absolute; left: 563px; top: 295px;
    list-style: none;
    font-size: 16px; color: var(--blue-text); line-height: 22px;
  }
</style>
</head>
<body>

<div class="side-label side-label--front">Front</div>

<section class="card card--front" aria-label="Card front">
  <svg class="card__lines" viewBox="0 0 827 447" aria-hidden="true">
    <line x1="215" y1="83" x2="561" y2="83" stroke="var(--trace)" stroke-width="4"/>
    <rect x="0" y="387" width="827" height="10" fill="var(--band-dark)"/>
    <rect x="0" y="402" width="827" height="45" fill="var(--band-light)"/>
  </svg>
  <div class="pulse-area pulse-area--front" role="img" aria-label="Heartbeat trace turning from jagged to smooth, with soft blue glow"></div>

  <div class="brand brand--front">
    <span class="brand__square"></span>
    <span class="brand__name">VitaBeat<span class="brand__reg">®</span></span>
  </div>

  <h1 class="role-title">Pulse Guide</h1>
  <p class="person-name">Merriwyn T. Hollingbeck</p>
  <p class="credentials">MSc, CWC, CSMCOSCA</p>
  <p class="certification">
    <span class="certification__badge"></span>Certified VitaBeat Practitioner
    <span class="certification__line2">&amp; Licensed Provider, QRX7318</span>
  </p>

  <ul class="contact">
    <li>07835 964 027</li>
    <li>Merriwyn@PulseGuide.co.uk</li>
    <li>www.PulseGuide.co.uk</li>
  </ul>
</section>

<section class="card card--back" aria-label="Card back">
  <svg class="card__lines" viewBox="0 0 826 449" aria-hidden="true">
    <g stroke="var(--trace)" stroke-width="4">
      <line x1="0" y1="57" x2="272" y2="57"/>
      <line x1="632" y1="47" x2="826" y2="47"/>
      <line x1="0" y1="177" x2="104" y2="177"/>
      <line x1="247" y1="177" x2="826" y2="177"/>
      <line x1="0" y1="301" x2="558" y2="301"/>
    </g>
    <rect x="0" y="411" width="826" height="10" fill="var(--band-dark)"/>
    <rect x="0" y="426" width="826" height="23" fill="var(--band-light)"/>
  </svg>
  <div class="pulse-area pulse-area--upper" role="img" aria-label="Appreciation heart rhythm trace with soft blue glow"></div>
  <div class="pulse-area pulse-area--middle" role="img" aria-label="Frustration heart rhythm trace, sharp jagged peaks"></div>
  <div class="pulse-area pulse-area--lower" role="img" aria-label="Heartbeat trace settling from jagged to smooth, with soft blue glow"></div>

  <div class="brand brand--back">
    <span class="brand__square"></span>
    <span class="brand__name">VitaBeat</span>
  </div>
</section>

<div class="side-label side-label--back">Back</div>

</body>
</html>
```